Quorvel Marketing & Design needs a Wordpress website

We need a wordpress design for a new marketing and design company in Australia called 'Quorvel Marketing & Design". The website needs to be responsive, modern, and attract new customers. It needs to be unique and different. We provide marketing and design solutions for small businesses from consulting, to flyer distribution to Feedcircle ads etc. We would like to see designs that use the Quorvel logo colours. The final design should communicate professionalism, creativity & growth. It needs to stand out from the crowd.

Target Market(s)

Small Business who need a marketing freelancer to help them grow

Industry/Entity Type

Marketing

Number of Pages Required

3 page

Requirements
Must have
• Home page, services page & contact page

```html
<!DOCTYPE html>
<html lang="en">
<head>
<meta charset="utf-8">
<title>Quorvel Marketing &amp; Design</title>
<link href="https://fonts.googleapis.com/css2?family=Roboto:wght@300;400;500;700&display=swap" rel="stylesheet">
<style>
:root{
  --magenta:#e5188a;
  --blush:#f6c9dc;
  --navy:#14163b;
  --navy-card:#1b1d48;
  --ink:#2a2a33;
  --muted:#6d6d78;
  --paper:#f4f4f6;
  --white:#ffffff;
}
*{margin:0;padding:0;box-sizing:border-box}
html,body{width:1200px;height:4156px;overflow:hidden}
body{font-family:'Roboto',sans-serif;background:var(--paper);color:var(--ink);position:relative}
.abs{position:absolute}
.center{left:0;width:1200px;text-align:center}
h2{font-weight:500;font-size:36px;letter-spacing:1px;color:var(--ink)}
.lead{font-size:17px;line-height:30px;color:var(--ink)}

/* header + hero */
.hero{top:0;left:0;width:1200px;height:620px;clip-path:polygon(0 0,100% 0,100% 88%,50% 100%,0 88%);
  background:linear-gradient(120deg,#c7b8b8 0%,#e8dfe0 40%,#d7d2d6 70%,#b9b3b8 100%)}
.navbar{top:0;left:0;width:1200px;height:88px;background:rgba(246,201,220,.75)}
.brand{left:130px;top:18px;display:flex;align-items:center;gap:12px}
.brand-dot{width:50px;height:50px;border-radius:50%;background:var(--magenta)}
.brand-name{font-size:30px;font-weight:700;color:var(--navy);line-height:30px}
.brand-sub{font-size:10px;font-weight:500;color:var(--magenta);letter-spacing:1px}
.nav{right:120px;top:48px;display:flex;gap:40px;font-size:14px;color:var(--white);font-weight:500;letter-spacing:1px}
.hero-title{left:124px;top:352px;font-size:54px;font-weight:500;color:var(--navy);letter-spacing:1px;white-space:nowrap}
.hero-sub{left:240px;top:424px;font-size:21px;color:var(--navy)}
.btn{left:800px;top:384px;width:176px;height:60px;background:var(--blush);color:var(--white);font-size:18px;display:flex;align-items:center;justify-content:center;letter-spacing:1px}

/* about */
.service{width:300px;text-align:center}
.service svg{display:block;margin:0 auto 12px}
.service h3{font-size:17px;font-weight:700;margin-bottom:10px}
.service p{font-size:13px;line-height:20px;color:var(--muted)}

/* team */
.team-card{background:#3a3f5a}
.team-photo{width:100%;height:100%;background:linear-gradient(160deg,#4b4f6a,#262a45)}
.team-social{position:absolute;left:0;width:100%;top:45%;display:flex;justify-content:center;gap:24px}
.team-social span{width:30px;height:30px;border:3px solid var(--white);border-radius:4px}
.team-name{position:absolute;left:0;width:100%;background:var(--magenta);color:var(--white);text-align:center;font-size:14px;line-height:22px;padding:8px 0}
.arrow{stroke:#555;stroke-width:3;fill:none}

/* facts */
.facts{top:1656px;left:0;width:1200px;height:630px;clip-path:polygon(0 10%,50% 0,100% 10%,100% 90%,50% 100%,0 90%);
  background:linear-gradient(120deg,#3d3a3c,#6b6567 45%,#3e3b3d)}
.fact{top:1944px;width:224px;height:180px;background:var(--navy-card);color:var(--white);text-align:center}
.fact b{display:block;font-size:56px;font-weight:500;margin-top:32px}
.fact span{font-size:15px}

/* clients */
.client-photo{left:520px;top:2468px;width:160px;height:160px;border-radius:50%;border:4px solid var(--white);background:linear-gradient(#d9d3d6,#a7a0a5)}

/* connect */
.connect{top:2836px;left:0;width:1200px;height:440px;background:var(--navy)}
.social{top:3050px;width:160px;text-align:center}
.social i{display:block;width:64px;height:64px;border-radius:50%;border:3px solid var(--white);margin:0 auto 14px}
.social b{display:block;font-size:11px;font-weight:500;color:var(--magenta);letter-spacing:1px}
.social span{font-size:12px;color:#c9cad8}

/* partners */
.partners{left:200px;top:3412px;width:792px;height:180px;border:3px solid var(--navy);background:var(--white);display:flex;align-items:center;justify-content:space-around}
.partner{display:flex;align-items:center;gap:10px;font-size:20px;font-weight:700;color:var(--navy)}
.partner i{width:26px;height:26px;background:var(--navy)}

/* contact */
.contact{top:3620px;left:0;width:1200px;height:480px;clip-path:polygon(0 0,50% 14%,100% 0,100% 100%,0 100%);
  background:linear-gradient(110deg,#e7c9d4,#f7dde7 45%,#e9bfcf)}
.contact-item{top:3904px;display:flex;align-items:center;gap:18px;font-size:17px;color:var(--ink)}
.footer{top:4100px;left:0;width:1200px;height:56px;background:var(--navy);color:#c9cad8;font-size:12px;display:flex;align-items:center;justify-content:center}
</style>
</head>
<body>

<section class="abs hero" role="img" aria-label="Photo of a creative team working together at a desk"></section>
<header class="abs navbar"></header>
<div class="abs brand"><span class="brand-dot"></span><div><div class="brand-name">Quorvel</div><div class="brand-sub">MARKETING &amp; DESIGN</div></div></div>
<nav class="abs nav"><span>HOME</span><span>ABOUT</span><span>SERVICES</span><span>PORTFOLIO</span><span>CONTACTS</span></nav>
<h1 class="abs hero-title">BUSINESS SOLUTIONS</h1>
<p class="abs hero-sub">The most ambitious company</p>
<div class="abs btn">READ MORE</div>

<h2 class="abs center" style="top:676px">ABOUT QUORVEL</h2>
<p class="abs center lead" style="top:730px">We are a marketing agency located in AUSTRALIA We've won a ton of awards<br>and have been featured in all of the magazines.</p>

<div class="abs service" style="left:90px;top:850px">
  <svg width="48" height="64" viewBox="0 0 48 64"><circle cx="24" cy="22" r="18" fill="none" stroke="#14163b" stroke-width="6"/><circle cx="24" cy="22" r="7" fill="#14163b"/><path d="M12 36 L6 62 L24 52 L42 62 L36 36" fill="#14163b"/></svg>
  <h3>BRANDING</h3><p>Clear brand identities that make small businesses<br>easy to remember and trust.</p>
</div>
<div class="abs service" style="left:450px;top:880px">
  <svg width="48" height="60" viewBox="0 0 48 60"><path d="M24 4a17 17 0 0 0-10 31v8h20v-8A17 17 0 0 0 24 4z" fill="#14163b"/><rect x="16" y="47" width="16" height="5" fill="#14163b"/><rect x="18" y="54" width="12" height="4" fill="#14163b"/></svg>
  <h3>MARKETING</h3><p>Targeted campaigns, flyers and social ads<br>that bring new customers through.</p>
</div>
<div class="abs service" style="left:822px;top:850px">
  <svg width="60" height="50" viewBox="0 0 60 50"><path d="M4 18h12l30-14v42L16 32H4z" fill="#14163b"/><rect x="10" y="32" width="8" height="16" fill="#14163b"/><path d="M50 16l8-4M50 25h9M50 34l8 4" stroke="#14163b" stroke-width="4"/></svg>
  <h3>PROMOTION</h3><p>Local promotion and distribution plans built<br>around your budget and goals.</p>
</div>

<h2 class="abs center" style="top:1136px">OUR TEAM</h2>
<p class="abs center lead" style="top:1182px">We believe in a diverse range of personnel to bring creative skills, thoughts, and<br>ideas to the table.</p>

<svg class="abs" style="left:124px;top:1350px" width="30" height="60"><path class="arrow" d="M24 4 L6 30 L24 56"/></svg>
<svg class="abs" style="left:1046px;top:1350px" width="30" height="60"><path class="arrow" d="M6 4 L24 30 L6 56"/></svg>

<div class="abs team-card" style="left:188px;top:1260px;width:264px;height:320px">
  <div class="team-photo" role="img" aria-label="Portrait of team member"></div>
  <div class="team-social"><span></span><span></span></div>
  <div class="team-name" style="top:262px">Mara Lindqvist<br>CEO</div>
</div>
<div class="abs team-card" style="left:472px;top:1314px;width:260px;height:320px">
  <div class="team-photo" role="img" aria-label="Portrait of team member"></div>
  <div class="team-social"><span></span><span></span></div>
  <div class="team-name" style="top:262px">Mara Lindqvist<br>CEO</div>
</div>
<div class="abs team-card" style="left:752px;top:1260px;width:260px;height:320px">
  <div class="team-photo" role="img" aria-label="Portrait of team member"></div>
  <div class="team-social"><span></span><span></span></div>
  <div class="team-name" style="top:262px">Mara Lindqvist<br>CEO</div>
</div>

<section class="abs facts" role="img" aria-label="Photo of an office workspace, darkened"></section>
<h2 class="abs center" style="top:1786px;color:#fff">SOME FACTS ABOUT US</h2>
<p class="abs center lead" style="top:1836px;color:#e4e4ea;font-size:16px;line-height:26px">We measure every campaign we run and share honest numbers<br>with every client we work with.</p>
<div class="abs fact" style="left:128px"><b>120</b><span>Coffees Brewed</span></div>
<div class="abs fact" style="left:368px"><b>96</b><span>Clients Worked With</span></div>
<div class="abs fact" style="left:608px"><b>53</b><span>Completed Projects</span></div>
<div class="abs fact" style="left:848px"><b>7</b><span>Winning Awards</span></div>

<h2 class="abs center" style="top:2346px">HAPPY CLIENTS</h2>
<p class="abs center lead" style="top:2398px">Over 577 extremely satisfied clients!</p>
<svg class="abs" style="left:110px;top:2518px" width="30" height="60"><path class="arrow" d="M24 4 L6 30 L24 56"/></svg>
<svg class="abs" style="left:1040px;top:2518px" width="30" height="60"><path class="arrow" d="M6 4 L24 30 L6 56"/></svg>
<div class="abs client-photo" role="img" aria-label="Portrait of a happy client"></div>
<p class="abs lead" style="left:270px;width:660px;top:2648px;text-align:center;font-size:15px;line-height:26px;color:var(--muted)">Working with the team changed how our shop reaches people. They planned our flyers, ran our social ads and kept us updated every week. Our bookings doubled within three months and we finally have a brand we are proud to show.</p>
<p class="abs center" style="top:2750px;font-size:15px;font-weight:700">TESSA MARLOW, CAFE OWNER</p>

<section class="abs connect"></section>
<h2 class="abs center" style="top:2966px;color:#fff">GET CONNECTED</h2>
<div class="abs social" style="left:84px"><i></i><b>FEEDCIRCLE</b><span>Join the conversation</span></div>
<div class="abs social" style="left:296px"><i></i><b>CHIRPWAVE</b><span>Get the latest news</span></div>
<div class="abs social" style="left:520px"><i></i><b>PLUSRING</b><span>Connect with us</span></div>
<div class="abs social" style="left:744px"><i></i><b>CLIPSTREAM</b><span>View exclusive videos</span></div>
<div class="abs social" style="left:956px"><i></i><b>SNAPGRID</b><span>Latest images</span></div>

<h2 class="abs center" style="top:3312px;font-size:32px">WE WORK WITH</h2>
<p class="abs center lead" style="top:3358px;font-size:15px">Leaders of business trust us</p>
<div class="abs partners">
  <div class="partner"><i></i>Brightpath</div>
  <div class="partner"><i></i>Terraview</div>
  <div class="partner">Orbitly</div>
  <div class="partner">Harbourline</div>
</div>

<section class="abs contact" role="img" aria-label="Photo of hands typing on a laptop in soft pink light"></section>
<h2 class="abs center" style="top:3776px">CONTACT US</h2>
<div class="abs contact-item" style="left:120px"><svg width="20" height="28" viewBox="0 0 20 28"><path d="M10 0a10 10 0 0 0-10 10c0 8 10 18 10 18s10-10 10-18A10 10 0 0 0 10 0z" fill="#14163b"/><circle cx="10" cy="10" r="4" fill="#f6dbe6"/></svg>Australia, Wattle Lane, 12</div>
<div class="abs contact-item" style="left:480px"><svg width="28" height="20" viewBox="0 0 28 20"><rect width="28" height="20" fill="#14163b"/><path d="M1 1l13 10L27 1" stroke="#f6dbe6" stroke-width="2" fill="none"/></svg>hello@quorvel.example</div>
<div class="abs contact-item" style="left:912px"><svg width="24" height="24" viewBox="0 0 24 24"><path d="M5 1l5 5-3 3a14 14 0 0 0 8 8l3-3 5 5-3 4C10 23 1 14 1 4z" fill="#14163b"/></svg>555-01-27-48</div>

<footer class="abs footer">© 2015 Quorvel . All rights reserved.</footer>

</body>
</html>
```